Quorvane Stationery

New startup called Quorvane (calm + insight) will primarily operate in the sustainable / responsible investment space. It will inform investors on optimising their investments as well as advise businesses on becoming better investment prospects.
The Zen is represents "low stress", calmness, quiet confidence. The intelligence refers to analytics, informed decisions, reliable, consistent.

The responsible / sustainable business space is one that balances financial success with progressing society and protecting nature. It understands that society needs a healthy natural environment to survive and financial success in the long term depends on a smooth functioning social context.

Beyond these elements it is desirable for the design to communicate integrity, trust, partner, collaboration, innovation, growth.

Please note: separate contest (#752143) for business card design
Updates

Project Deadline Extended
Reason: The design of these artefacts should probably align with the business card being designed in parallel running project 752143.

Target Market(s)

Medium sized businesses
Wealth optimising and ethical / responsible investors

Industry/Entity Type

Environment

Font styles to use
Other font styles liked:
• Rounded as on logo and back of business card

Requirements
Must have
• Must use attached logo
Templates:
- Letterhead and continuation (footers welcomed) (Word, A4, editable text)
- Comp slip
- Envelopes (DL)
- Notepad
- Email signature (Outlook)
- Report cover & continuation pages (Word, A4, editable text)
- Presentation pack (PowerPoint)

```html
<!DOCTYPE html>
<html lang="en">
<head>
<meta charset="utf-8">
<title>Quorvane Stationery</title>
<link rel="stylesheet" href="https://fonts.googleapis.com/css2?family=Nunito:wght@600&family=Josefin+Sans:ital,wght@0,700;1,400&family=Crimson+Text:wght@400;600&display=swap">
<style>
  :root {
    --blue: #3568b4;
    --orange: #f68b28;
    --green: #9cc83b;
    --ink: #111111;
    --brand-grey: #555a60;
    --paper: #ffffff;
    --backdrop: #e4e4e4;
    --logo-font: "Nunito", sans-serif;
    --body-font: "Josefin Sans", sans-serif;
    --detail-font: "Crimson Text", serif;
  }
  * { box-sizing: border-box; margin: 0; padding: 0; }
  html, body { width: 1200px; height: 900px; overflow: hidden; }
  body { background: var(--backdrop); position: relative; }

  .sheet { position: absolute; background: var(--paper); overflow: hidden; }

  /* right-edge colour stripes */
  .edge-stripes { position: absolute; top: 0; right: 0; height: 100%; display: flex; }
  .edge-stripes span { display: block; height: 100%; }
  .edge-stripes .stripe-blue { background: var(--blue); }
  .edge-stripes .stripe-orange { background: var(--orange); }
  .edge-stripes .stripe-green { background: var(--green); }
  .edge-stripes.faded { opacity: 0.3; }

  .brand { position: absolute; display: flex; align-items: center; gap: 5px;
           font-family: var(--logo-font); font-weight: 600; color: var(--brand-grey); white-space: nowrap; }
  .brand .dot { border-radius: 50%; background: var(--blue); flex: none; }

  /* business cards */
  .card-front { left: 30px; top: 127px; width: 298px; height: 170px; }
  .card-back  { left: 30px; top: 329px; width: 298px; height: 170px; }

  .contact { position: absolute; color: var(--ink); font-family: var(--detail-font); }
  .contact .name { font-family: var(--body-font); font-weight: 700; }
  .contact .role { font-weight: 600; letter-spacing: 0.5px; }
  .card-back .contact { left: 12px; top: 16px; font-size: 10.5px; line-height: 1.2; }
  .card-back .contact .name { font-size: 14px; margin-bottom: 2px; }
  .card-back .contact .role { font-size: 16px; line-height: 1; margin-bottom: 2px; }

  /* report cover */
  .cover { left: 371px; top: 63px; width: 306px; height: 434px; }

  /* letterhead */
  .letterhead { left: 723px; top: 62px; width: 308px; height: 440px; }
  .letter-body { position: absolute; left: 17px; top: 108px; width: 252px;
                 font-family: var(--body-font); font-style: italic; font-size: 11px;
                 line-height: 17px; text-align: justify; color: var(--ink); }

  .mini-contact { font-size: 5px; line-height: 1.15; }
  .mini-contact .name { font-size: 6px; }
  .mini-contact .role { font-size: 7px; line-height: 1; }

  /* envelopes */
  .envelope { top: 541px; width: 422px; height: 254px; }
  .envelope-front { left: 273px; }
  .envelope-back { left: 723px; }
</style>
</head>
<body>

<!-- Business card front -->
<div class="sheet card-front">
  <div class="brand" style="left:14px; top:18px; font-size:11px;"><span class="dot" style="width:14px;height:14px;"></span>quorvane</div>
  <div class="edge-stripes" aria-hidden="true">
    <span class="stripe-green" style="width:8px"></span>
    <span class="stripe-orange" style="width:10px"></span>
    <span class="stripe-blue" style="width:16px"></span>
  </div>
</div>

<!-- Business card back -->
<div class="sheet card-back">
  <div class="contact">
    <p class="name">Daniel Hart</p>
    <p>academic qualifications</p>
    <p class="role">DIRECTOR</p>
    <p>Tel : 127 555 0142</p>
    <p>Email : info@quorvane.com</p>
    <p>www.quorvane.com.eu</p>
  </div>
  <div class="brand" style="left:12px; top:130px; font-size:8px;"><span class="dot" style="width:10px;height:10px;"></span>quorvane</div>
  <div class="edge-stripes" aria-hidden="true">
    <span class="stripe-green" style="width:8px"></span>
    <span class="stripe-orange" style="width:10px"></span>
    <span class="stripe-blue" style="width:16px"></span>
  </div>
</div>

<!-- Report cover -->
<div class="sheet cover">
  <div class="brand" style="left:22px; top:190px; font-size:17px; gap:7px;"><span class="dot" style="width:24px;height:24px;"></span>quorvane</div>
  <div class="edge-stripes" aria-hidden="true">
    <span class="stripe-green" style="width:22px"></span>
    <span class="stripe-orange" style="width:28px"></span>
    <span class="stripe-blue" style="width:44px"></span>
  </div>
</div>

<!-- Letterhead -->
<div class="sheet letterhead">
  <div class="edge-stripes faded" aria-hidden="true">
    <span class="stripe-green" style="width:6px"></span>
    <span class="stripe-orange" style="width:8px"></span>
    <span class="stripe-blue" style="width:12px"></span>
  </div>
  <div class="brand" style="left:16px; top:26px; font-size:10px;"><span class="dot" style="width:14px;height:14px;"></span>quorvane</div>
  <div class="letter-body">
    <p>New startup called Quorvane will primarily operate in the sustainable / responsible investment space. It will inform investors on optimising their investments as well as advise businesses on becoming better investment prospects.</p>
    <p>The calm side represents "low stress", steadiness, quiet confidence. The insight side refers to analytics, informed decisions, reliable, consistent.</p>
  </div>
  <div class="brand" style="left:18px; top:362px; font-size:5px; gap:3px;"><span class="dot" style="width:7px;height:7px;"></span>quorvane</div>
  <div class="contact mini-contact" style="left:18px; top:385px;">
    <p class="name">Daniel Hart</p>
    <p>academic qualifications</p>
    <p class="role">DIRECTOR</p>
    <p>Tel : 127 555 0142</p>
    <p>Email : info@quorvane.com</p>
    <p>www.quorvane.com.eu</p>
  </div>
</div>

<!-- Envelope front -->
<div class="sheet envelope envelope-front">
  <div class="brand" style="left:23px; top:30px; font-size:11px;"><span class="dot" style="width:16px;height:16px;"></span>quorvane</div>
  <div class="edge-stripes" aria-hidden="true">
    <span class="stripe-green" style="width:12px"></span>
    <span class="stripe-orange" style="width:16px"></span>
    <span class="stripe-blue" style="width:26px"></span>
  </div>
</div>

<!-- Envelope back -->
<div class="sheet envelope envelope-back">
  <div class="brand" style="left:36px; top:160px; font-size:6px; gap:3px;"><span class="dot" style="width:10px;height:10px;"></span>quorvane</div>
  <div class="contact mini-contact" style="left:38px; top:196px;">
    <p class="name">Daniel Hart</p>
    <p>academic qualifications</p>
    <p class="role">DIRECTOR</p>
    <p>Tel : 127 555 0142</p>
    <p>Email : info@quorvane.com</p>
    <p>www.quorvane.com.eu</p>
  </div>
  <div class="edge-stripes" aria-hidden="true">
    <span class="stripe-green" style="width:12px"></span>
    <span class="stripe-orange" style="width:16px"></span>
    <span class="stripe-blue" style="width:26px"></span>
  </div>
</div>

</body>
</html>
```